Business Card Design

We are a motorcycle parts, spares, accessories and workshop as well as a vq dealership. We mostly specialize in dirt bikes. I have uploaded a pic of bikes lined up at the starting gate. I envisage having the picture as a backboard maybe out of focus with the logo at the top of the card and the details off to the right side.

Target Market(s)

Male Motorcycle enthusiast aged 18-35

Industry/Entity Type

Business

Contact Information for Business Card

8/314 Pelican Ridge Rd
Harlow Bend QLD 4106
Ph: (07) 3902 4157
Email: lorna@kerbstonegear.com.au
www.kerbstonegear.com.au

Requirements
Must have
• on the rear side of the card lines for writing

```html
<!DOCTYPE html>
<html lang="en">
<head>
<meta charset="utf-8">
<title>Kerbstone Gear – Business Card</title>
<link href="https://fonts.googleapis.com/css2?family=Open+Sans:wght@600;700;800&display=swap" rel="stylesheet">
<style>
  :root {
    --backdrop: #121a1d;
    --card-white: #ffffff;
    --card-grey-light: #eef0f2;
    --card-grey-mid: #b9bdc1;
    --card-grey-dark: #8d9296;
    --ink: #111418;
    --rule: #f4f4f4;
    --dotted: #8a8a8a;
    --mark-grey: #9a9ea2;
    --photo-blue: #3f5fa8;
    --photo-red: #c9646e;
    --photo-steel: #a7abb0;
  }
  html, body {
    margin: 0;
    padding: 0;
    width: 1200px;
    height: 801px;
    overflow: hidden;
    background: var(--backdrop);
    font-family: "Open Sans", Arial, sans-serif;
  }
  .canvas {
    position: relative;
    width: 1200px;
    height: 801px;
  }
  .card {
    position: absolute;
    top: 245px;
    overflow: hidden;
  }
  .card--front {
    left: 111px;
    width: 473px;
    height: 304px;
    background:
      radial-gradient(ellipse at 70% 20%, var(--card-grey-light) 0%, rgba(238,240,242,0) 55%),
      linear-gradient(160deg, var(--card-grey-light) 0%, var(--card-grey-mid) 50%, var(--card-grey-dark) 100%);
  }
  .card--back {
    left: 617px;
    width: 477px;
    height: 308px;
    background: var(--card-white);
  }
  .front__photo {
    position: absolute;
    left: 0;
    top: 56px;
    width: 300px;
    height: 192px;
    background: linear-gradient(180deg, var(--photo-blue) 0%, var(--photo-red) 22%, var(--photo-steel) 55%, var(--photo-red) 85%, var(--photo-steel) 100%);
    -webkit-mask-image: linear-gradient(90deg, #000 45%, transparent 100%);
    mask-image: linear-gradient(90deg, #000 45%, transparent 100%);
  }
  .front__rule {
    position: absolute;
    left: 0;
    height: 1px;
    background: var(--rule);
  }
  .front__rule--top { top: 56px; width: 435px; }
  .front__rule--bottom { top: 248px; width: 267px; }
  .brand {
    position: absolute;
    left: 146px;
    top: 98px;
    display: flex;
    align-items: center;
    gap: 10px;
    white-space: nowrap;
  }
  .brand__square {
    width: 20px;
    height: 20px;
    background: var(--ink);
    flex: none;
  }
  .brand__name {
    font-weight: 800;
    font-size: 28px;
    line-height: 1;
    color: var(--ink);
    letter-spacing: 0.3px;
  }
  .tagline {
    position: absolute;
    right: 50px;
    top: 141px;
    font-weight: 800;
    font-size: 12.5px;
    line-height: 15px;
    color: var(--ink);
    letter-spacing: 0.3px;
    white-space: nowrap;
  }
  .contact {
    position: absolute;
    right: 42px;
    text-align: right;
    font-weight: 700;
    font-size: 12.5px;
    line-height: 15px;
    color: var(--ink);
    margin: 0;
    white-space: nowrap;
  }
  .contact--address { top: 186px; }
  .contact--phone { top: 228px; }
  .contact--web { top: 255px; }
  .back__line {
    position: absolute;
    left: 29px;
    right: 33px;
    border-top: 1px dotted var(--dotted);
  }
  .back__line--short { right: 169px; }
  .back__mark {
    position: absolute;
    right: 31px;
    top: 259px;
    font-weight: 800;
    font-size: 17px;
    color: var(--mark-grey);
    letter-spacing: 0.5px;
  }
</style>
</head>
<body>
<main class="canvas">
  <section class="card card--front" aria-label="Business card front">
    <div class="front__photo" role="img" aria-label="Photo of dirt bikes lined up at the starting gate"></div>
    <div class="front__rule front__rule--top"></div>
    <div class="front__rule front__rule--bottom"></div>
    <div class="brand">
      <span class="brand__square"></span>
      <span class="brand__name">KERBSTONE GEAR</span>
    </div>
    <div class="tagline">REPAIRS - SALES - SERVICE</div>
    <p class="contact contact--address">8/314 Pelican Ridge Rd<br>Harlow Bend QLD 4106</p>
    <p class="contact contact--phone">Ph: (07) 3902 4157</p>
    <p class="contact contact--web">Email: lorna@kerbstonegear.com.au<br>www.kerbstonegear.com.au</p>
  </section>

  <section class="card card--back" aria-label="Business card back with writing lines">
    <div class="back__line" style="top:64px"></div>
    <div class="back__line" style="top:99px"></div>
    <div class="back__line" style="top:133px"></div>
    <div class="back__line" style="top:167px"></div>
    <div class="back__line" style="top:202px"></div>
    <div class="back__line" style="top:237px"></div>
    <div class="back__line back__line--short" style="top:271px"></div>
    <div class="back__mark">KERBSTONE</div>
  </section>
</main>
</body>
</html>
```